Cannabis Glass Jar Label for California Cannabis Company

Design a Glass jar label for Brisk Canopy Co. marijuana flower. Our brand is meant to be bold, vibrant and inspiring. The contents of the jar is a premium cannabis flower from a strain called "Velvet Figs". The design should reflect the high quality of the product and reflect the strain name "Velvet Figs" visually. The use of a Lemon with gold dripping or something similar is encouraged.

Target Market(s)

Cannabis users between 24-35

Industry/Entity Type

California Cannabis

Font styles to use
Other font styles liked:
• Montserrat

Colors
0054AA
0677BA
7BADD7
CADEEF
E8F1F8
FFC000
F8CF3A
FAE287
FDF2CF
FEFAEE
6B429C
8869AF
B7A5CE
E3DAEB
F3F0F8

Requirements
Must have
• Compliance information and dimensions provided in template, all text provided in template (although layout can change), Name: Velvet Figs
Nice to have
• Lemon dripping gold, play between realism and graphic art
Should not have
• Cartoons, Animals,

```html
<!DOCTYPE html>
<html lang="en">
<head>
<meta charset="utf-8">
<title>Velvet Figs – Jar Label</title>
<link rel="stylesheet" href="https://fonts.googleapis.com/css2?family=Montserrat:wght@300;400;600;700;800&family=Source+Sans+3:wght@400&display=swap">
<style>
  :root {
    --cream: #FDF2CF;
    --gold: #FFC000;
    --gold-soft: #F8CF3A;
    --gold-panel: #FCCF48;
    --white: #FFFFFF;
    --ink: #3A3A3A;
    --grey-mark: #6E6A60;
    --photo-top: #F6B80E;
    --photo-mid: #FBD65A;
  }
  * { margin: 0; padding: 0; box-sizing: border-box; }
  html, body { width: 1200px; height: 300px; overflow: hidden; background: var(--cream); }
  .label {
    position: relative; width: 1200px; height: 300px;
    background: var(--cream);
    font-family: "Montserrat", sans-serif;
  }
  .gov-warning {
    position: absolute; left: 19px; top: 20px; width: 303px; height: 265px;
    background: var(--gold-panel); border-radius: 20px;
    display: flex; align-items: center; justify-content: center;
  }
  .gov-warning p {
    font-family: "Source Sans 3", sans-serif; font-size: 11.6px; line-height: 15px;
    color: var(--white); text-align: center; text-transform: uppercase;
    letter-spacing: -0.3px; white-space: nowrap;
  }
  .fruit-photo {
    position: absolute; left: 463px; top: 0; width: 410px; height: 300px;
    background: linear-gradient(180deg, var(--photo-top) 0%, var(--photo-mid) 45%, var(--cream) 100%);
  }
  .universal-mark { position: absolute; left: 342px; top: 220px; width: 64px; height: 70px; }
  .product-name {
    position: absolute; left: 455px; top: 221px; width: 420px; text-align: center;
    font-weight: 700; font-size: 48px; line-height: 48px; letter-spacing: 0.5px; color: var(--gold);
  }
  .net-weight {
    position: absolute; left: 701px; top: 273px;
    font-weight: 700; font-size: 10px; color: var(--gold);
  }
  .socials {
    position: absolute; left: 948px; top: 16px; display: flex; gap: 10px; align-items: center;
    font-size: 9px; font-weight: 400; color: var(--ink);
  }
  .social { display: flex; align-items: center; gap: 3px; }
  .social-dot { width: 19px; height: 19px; border: 1.5px solid var(--ink); border-radius: 50%; }
  .social-dot.square { border-radius: 4px; }
  .mission {
    position: absolute; left: 947px; top: 47px; width: 218px; height: 198px;
    border: 2px solid var(--white); border-radius: 20px;
    padding: 14px 4px 0; text-align: center;
  }
  .mission h2 {
    font-size: 12px; font-weight: 700; line-height: 15px; color: var(--gold);
  }
  .mission p {
    margin-top: 9px; font-size: 10.6px; font-weight: 400; line-height: 13px;
    color: var(--gold-soft); white-space: nowrap;
  }
  .prop-warning {
    position: absolute; left: 964px; top: 254px; width: 190px;
    display: flex; align-items: center; gap: 8px;
    font-size: 7px; line-height: 9px; color: var(--ink);
  }
  .prop-warning span { text-align: center; flex: 1; }
  .maker {
    position: absolute; left: 963px; top: 277px; font-size: 11px; font-weight: 400; color: var(--ink);
  }
</style>
</head>
<body>
<main class="label">
  <section class="gov-warning">
    <p>Government warning: this package<br>contains cannabis, a schedule I<br>controlled substance. Keep out of<br>reach of children and animals.<br>Cannabis may only be possessed or<br>consumed by persons 21 years of age<br>or older unless the person is a<br>qualified patient. Cannabis use while<br>pregnant or breastfeeding may be<br>harmful. Consumption of cannabis<br>impairs your ability to drive and<br>operate machinery. Please use<br>extreme caution.</p>
  </section>

  <div class="fruit-photo" role="img" aria-label="Photograph of a sliced citrus fruit dripping golden honey"></div>

  <svg class="universal-mark" viewBox="0 0 64 70" role="img" aria-label="Universal product symbol">
    <path d="M32 4 L60 50 H4 Z" fill="none" stroke="var(--grey-mark)" stroke-width="4" stroke-linejoin="round"/>
  </svg>

  <h1 class="product-name">VELVET FIGS</h1>
  <div class="net-weight">NET WT. 4.0 oz (113.4g)</div>

  <div class="socials">
    <div class="social"><span class="social-dot square"></span>@brisk_canopy_co</div>
    <div class="social"><span class="social-dot"></span>briskcanopy.co</div>
  </div>

  <section class="mission">
    <h2>YOU ARE CAPABLE<br>OF GREATNESS</h2>
    <p>We are here to elevate you to<br>your highest and inspire you to<br>pursue your dreams. Our<br>handcrafted, curated selection<br>of cultivars is our passion, our<br>call to greatness, and with each<br>strain we hope to propel you<br>towards yours. Live your best<br>life. Find your passion. Elevate<br>your canopy.</p>
  </section>

  <div class="prop-warning">
    <svg width="17" height="15" viewBox="0 0 17 15" aria-hidden="true">
      <path d="M8.5 1 L16 14 H1 Z" fill="var(--gold)" stroke="#222" stroke-width="1.2" stroke-linejoin="round"/>
      <rect x="7.8" y="5" width="1.4" height="5" fill="#222"/>
      <rect x="7.8" y="11" width="1.4" height="1.4" fill="#222"/>
    </svg>
    <span>WARNING: Cancer and reproductive harm<br>www.LabelNotices.ca.gov</span>
  </div>
  <div class="maker">Tallow Ridge Growers, LLC 279-555-0147</div>
</main>
</body>
</html>
```